Italian / Pizza Catering Menu*

Catering Menu for Businesses .... must be clean, crispy, attractive

Want a Tri-Fold Catering Menu - See photos of Existing - see attached for content and format - but do NOT want same photos....need fresh and crisp looking foods- dislike the green

Note the front fold - it say Italian Catering

Also attached is the new Tri Fold Menu - so can get a feel for the new look

If you need high res photos, food photos, these can be uploaded - or you can use third party but must be italian food pizza related and look like our food.

Target Market(s)

Businesses to place Catering Orders

Logo Text

Fresh Catering

Logo styles of interest
Pictorial/Combination Logo
Font styles to use
Sans Serif

Requirements
Must have
• Food Photos
Pop
Fresh

Should Focus on Fast & Fresh

Also note that the catering will be offered from the following locations -

Heights 281-555-0143
3916 Copper Fen Drive, Houston, TX 77007

Brindle 713-555-0178
418 Brindle Street, Houston, TX 77002

VelT 713-555-0126
5410 Marden Parkway, #340, Houston, TX 77024

Sienna Plantation 281-555-0192
20475 Hwy 14, Ste K, Missouri City TX 77459

Pflugerville 512-555-0164
27403 Granary Business Dr #300, Pflugerville TX 78660

Delete - Franchise Opportunities information
Nice to have
• Color

```html
<!DOCTYPE html>
<html lang="en">
<head>
<meta charset="utf-8">
<title>Rinaldi's Pizzeria – Catering Menu</title>
<link href="https://fonts.googleapis.com/css2?family=Oswald:wght@400;500;600;700&family=Roboto+Condensed:wght@400;700&family=Kaushan+Script&family=Cinzel:wght@700&display=swap" rel="stylesheet">
<style>
  :root{
    --stage:#c92530;
    --panel:#252325;
    --panel-stripe:#2b292b;
    --red:#c8202c;
    --red-dark:#9c1a23;
    --white:#ffffff;
    --muted:#bdb7b7;
    --gold:#e6b422;
    --photo-warm:#6b3a22;
    --photo-dark:#1a1412;
  }
  *{box-sizing:border-box;margin:0;padding:0}
  html,body{width:1200px;height:1000px;overflow:hidden}
  body{background:var(--stage);font-family:"Roboto Condensed",sans-serif;color:var(--white);position:relative}

  .trifold{position:absolute;left:30px;top:60px;width:1140px;height:880px;display:flex;box-shadow:0 20px 40px rgba(0,0,0,.35)}
  .panel{position:relative;width:380px;height:880px;overflow:hidden;
    background:repeating-linear-gradient(90deg,var(--panel) 0 6px,var(--panel-stripe) 6px 12px)}
  .panel + .panel{border-left:1px solid #1a181a}

  .section-bar{background:var(--red);margin:22px 18px 0;padding:8px 10px;text-align:center;
    font-family:"Oswald",sans-serif;font-weight:600;font-size:22px;letter-spacing:.5px;text-transform:uppercase;border-radius:3px}
  .section-sub{text-align:center;font-size:11px;text-transform:uppercase;color:var(--muted);margin-top:6px;letter-spacing:.3px}

  /* Buffet packages */
  .package{display:flex;align-items:center;margin:22px 18px 0;height:165px;position:relative}
  .package-text{width:170px}
  .package-name{font-family:"Oswald",sans-serif;font-weight:600;font-size:16px;text-transform:uppercase;color:var(--white);margin-bottom:6px}
  .package-list{list-style:none;font-size:12px;line-height:1.6;color:var(--muted)}
  .price-badge{position:absolute;left:170px;top:14px;width:60px;height:60px;border-radius:50%;background:var(--red);
    display:flex;flex-direction:column;align-items:center;justify-content:center;z-index:2;border:2px solid var(--panel)}
  .price-badge b{font-family:"Oswald",sans-serif;font-size:19px;line-height:1}
  .price-badge small{font-size:8px;text-transform:uppercase}
  .package-photo{margin-left:auto;width:150px;height:150px;border-radius:6px;
    background:radial-gradient(circle at 50% 55%,#f1ece4 0 38%,#c9a27a 39% 48%,var(--photo-dark) 70%)}
  .panel-foot{position:absolute;left:18px;right:18px;bottom:26px;border-top:1px solid #444;padding-top:12px}
  .panel-foot h3{font-family:"Oswald",sans-serif;font-size:18px;color:var(--gold);text-transform:uppercase}
  .panel-foot p{font-size:12px;color:var(--muted)}

  /* Sandwich trays */
  .tray-row{display:flex;align-items:center;justify-content:space-around;margin:16px 18px 0}
  .tray{text-align:center;width:140px}
  .tray-name{font-family:"Oswald",sans-serif;font-size:14px;color:var(--red);text-transform:uppercase;line-height:1.15}
  .tray-serves{font-size:10px;color:var(--gold);text-transform:uppercase;margin-top:6px}
  .tray-detail{font-size:9px;color:var(--muted)}
  .tray-price{font-family:"Oswald",sans-serif;font-weight:700;font-size:40px;line-height:1.1}
  .tray-price sup{font-size:17px;vertical-align:20px}
  .tray-mix{font-size:10px;color:var(--red);text-transform:uppercase;margin-top:6px}
  .tray-items{list-style:none;font-size:10px;color:var(--muted);line-height:1.5}
  .or{font-size:13px;color:var(--muted)}
  .pizza-row{display:flex;justify-content:space-around;margin:14px 18px 0}
  .pizza{text-align:center;width:140px}
  .pizza-size{font-family:"Oswald",sans-serif;font-size:14px;color:var(--red)}
  .pizza-price{font-family:"Oswald",sans-serif;font-weight:700;font-size:30px;line-height:1.1}
  .pizza-price sup{font-size:14px;vertical-align:12px}
  .pizza-note{font-size:9px;color:var(--muted)}
  .side-note{text-align:center;font-size:10px;color:var(--muted);margin:10px 18px 0}
  .please-note{margin:8px 18px 0;font-size:9px;color:var(--muted)}
  .please-note b{color:var(--gold);font-family:"Oswald",sans-serif;font-size:12px;margin-right:4px}

  /* Hexagon feature */
  .hex-feature{position:absolute;left:0;bottom:40px;width:380px;height:300px}
  .hex-feature svg{display:block}

  /* Cover */
  .brand{display:flex;align-items:center;justify-content:center;gap:8px;margin-top:58px}
  .brand-mark{width:12px;height:12px;background:var(--red)}
  .brand-name{font-family:"Oswald",sans-serif;font-weight:600;font-size:30px;color:var(--white);letter-spacing:.5px}
  .kitchen-line{display:flex;justify-content:space-between;align-items:center;margin:12px 28px 0;
    font-family:"Cinzel",serif;font-size:15px;color:var(--gold)}
  .kitchen-line span{padding:3px 6px;border-top:2px solid var(--gold);border-bottom:2px solid var(--gold)}
  .tagline{font-family:"Kaushan Script",cursive;font-size:50px;text-align:center;margin-top:70px;line-height:1}
  .delivery-bar{margin:14px 48px 0;background:var(--red);text-align:center;padding:4px 0 5px;line-height:1.2}
  .delivery-bar b{display:block;font-family:"Oswald",sans-serif;font-size:13px;letter-spacing:.5px}
  .delivery-bar span{font-size:11px}
</style>
</head>
<body>
<main class="trifold">

  <!-- Buffet packages panel -->
  <section class="panel panel-buffet">
    <h2 class="section-bar">Rinaldi's Buffet Packages</h2>
    <p class="section-sub">Minimum order 20 people</p>

    <article class="package">
      <div class="package-text">
        <h3 class="package-name">Pasta to Table</h3>
        <ul class="package-list"><li>Choice of two pastas</li><li>House garden salad</li><li>Garlic knots</li><li>Plates &amp; utensils</li></ul>
      </div>
      <div class="price-badge"><b>8.95</b><small>per person</small></div>
      <div class="package-photo" role="img" aria-label="Photo of a plated creamy pasta dish"></div>
    </article>

    <article class="package">
      <div class="package-text">
        <h3 class="package-name">Hand Crafted</h3>
        <ul class="package-list"><li>Choice of two entrees</li><li>Caesar or garden salad</li><li>Fresh baked bread</li><li>Tiramisu cups</li></ul>
      </div>
      <div class="price-badge"><b>14.95</b><small>per person</small></div>
      <div class="package-photo" role="img" aria-label="Photo of a fresh Italian salad bowl"></div>
    </article>

    <article class="package">
      <div class="package-text">
        <h3 class="package-name">Chef's Table</h3>
        <ul class="package-list"><li>Three entree choices</li><li>Chicken wings platter</li><li>Antipasto salad</li><li>Cannoli tray</li></ul>
      </div>
      <div class="price-badge"><b>17.95</b><small>per person</small></div>
      <div class="package-photo" role="img" aria-label="Photo of a plate of chicken wings"></div>
    </article>

    <footer class="panel-foot">
      <h3>Party Size Trays</h3>
      <p>Free delivery &amp; set up</p>
    </footer>
  </section>

  <!-- Sandwich trays & pizzas panel -->
  <section class="panel panel-trays">
    <h2 class="section-bar">Italian Sandwich Trays</h2>
    <p class="section-sub">Serving size is based on two halves per person</p>

    <div class="tray-row">
      <div class="tray">
        <h3 class="tray-name">Cold<br>Sandwich<br>Tray</h3>
        <p class="tray-serves">Serves 4-6</p>
        <p class="tray-detail">Six sandwiches, twelve halves</p>
        <p class="tray-price">69<sup>95</sup></p>
        <p class="tray-mix">Mix &amp; Match</p>
        <ul class="tray-items"><li>Italian sub</li><li>Turkey &amp; provolone</li><li>Caprese</li></ul>
      </div>
      <span class="or">or</span>
      <div class="tray">
        <h3 class="tray-name">Hot<br>Sandwich<br>Tray</h3>
        <p class="tray-serves">Serves 4-6</p>
        <p class="tray-detail">Six sandwiches, twelve halves</p>
        <p class="tray-price">79<sup>95</sup></p>
        <p class="tray-mix">Mix &amp; Match</p>
        <ul class="tray-items"><li>Meatball parm</li><li>Chicken parm</li><li>Sausage &amp; peppers</li></ul>
      </div>
    </div>

    <h2 class="section-bar">Specialty Pizzas</h2>
    <p class="section-sub">Calorie counts for pizza are listed per slice</p>
    <p class="side-note">Add a side salad or dessert to any order</p>

    <div class="pizza-row">
      <div class="pizza">
        <h3 class="pizza-size">14" Medium</h3>
        <p class="pizza-price">$18<sup>95</sup></p>
        <p class="pizza-note">Cut into eight slices</p>
      </div>
      <div class="pizza">
        <h3 class="pizza-size">16" Large</h3>
        <p class="pizza-price">$22<sup>95</sup></p>
        <p class="pizza-note">Cut into ten slices</p>
      </div>
    </div>
    <p class="please-note"><b>PLEASE NOTE:</b>Orders require 24 hours notice. Prices subject to change without notice.</p>

    <div class="hex-feature">
      <svg width="380" height="300" viewBox="0 0 380 300">
        <defs>
          <radialGradient id="pizzaTone" cx="50%" cy="65%" r="60%">
            <stop offset="0" stop-color="#c4562a"/>
            <stop offset=".5" stop-color="var(--photo-warm)"/>
            <stop offset="1" stop-color="var(--photo-dark)"/>
          </radialGradient>
        </defs>
        <rect class="band" x="0" y="118" width="380" height="28" fill="var(--red-dark)"/>
        <rect class="band" x="0" y="160" width="380" height="28" fill="var(--red-dark)"/>
        <polygon points="115,10 265,10 340,150 265,290 115,290 40,150" fill="var(--red)"/>
        <polygon points="124,26 256,26 322,150 256,274 124,274 58,150" fill="url(#pizzaTone)" role="img" aria-label="Photo of a pepperoni pizza with flying pepper rings"/>
      </svg>
    </div>
  </section>

  <!-- Cover panel -->
  <section class="panel panel-cover">
    <div class="brand"><span class="brand-mark"></span><span class="brand-name">Rinaldi's Pizzeria</span></div>
    <div class="kitchen-line"><span>ITALIAN</span><span>KITCHEN</span></div>
    <h1 class="tagline">Fast &amp; Fresh</h1>
    <div class="delivery-bar"><b>FREE DELIVERY</b><span>rinaldispizza.com</span></div>

    <div class="hex-feature">
      <svg width="380" height="300" viewBox="0 0 380 300">
        <defs>
          <radialGradient id="coverTone" cx="50%" cy="70%" r="60%">
            <stop offset="0" stop-color="#b8682f"/>
            <stop offset=".5" stop-color="var(--photo-warm)"/>
            <stop offset="1" stop-color="var(--photo-dark)"/>
          </radialGradient>
        </defs>
        <rect x="0" y="100" width="380" height="34" fill="var(--red-dark)"/>
        <rect x="0" y="150" width="380" height="34" fill="var(--red-dark)"/>
        <polygon points="115,10 265,10 340,150 265,290 115,290 40,150" fill="var(--red)"/>
        <polygon points="124,26 256,26 322,150 256,274 124,274 58,150" fill="url(#coverTone)" role="img" aria-label="Photo of a pizza with toppings tossed in the air"/>
      </svg>
    </div>
  </section>

</main>
</body>
</html>
```